Website Redesign

I am looking to have our website redone. We recently paid to have this done and are very unhappy with the results. We're looking to have a much more modern and clean feeling while GREATLY enhancing the user experience. We are very close to have a new logo designed as well as having some brand colors (Pantone 3005C). We want our site to have a human feel to it without focusing completely on our products. That being said, we need our products to play a more prominent role as our current site doesn't very clearly display what we do.
Our website: kvhomewares.com
Websites we like (overall feel): jogluma.com, oswaldtrent.com
Websites we like (functionality): birchvault.com
Updates
I apologize, we are new to ArtHivePro. I am showing a budget of $500 for this project. I know we'd go beyond that. I do not believe that we'll be able to overhaul our website for $500. I apologize for any confusion.

```html
<!DOCTYPE html>
<html lang="en">
<head>
<meta charset="utf-8">
<title>KV Homewares – Lightweight Training Tables</title>
<link rel="stylesheet" href="https://fonts.googleapis.com/css2?family=Roboto:wght@400;500;700&display=swap">
<style>
:root{
  --brand:#0a74cf;
  --brand-dark:#0560b4;
  --brand-light:#8ccbf7;
  --tab-red:#f57c7a;
  --tab-violet:#7e8ef1;
  --ink:#333;
  --muted:#9a9a9a;
  --soft:#888;
  --line:#bdbdbd;
  --green:#5aae1e;
  --orange:#e0671b;
  --pdf:#c2141b;
  --white:#fff;
}
*{box-sizing:border-box;margin:0;padding:0}
html,body{width:1200px;height:750px;overflow:hidden;background:var(--white);font-family:"Roboto",Arial,sans-serif;color:var(--ink)}
.page{position:relative;width:1200px;height:750px}
.site-header{position:absolute;left:0;top:0;width:1200px;height:58px;background:var(--brand)}
.logo-fold{position:absolute;left:0;top:0}
.brand-name{position:absolute;left:205px;top:14px;color:var(--white);font-size:22px;font-weight:500;line-height:1}
.brand-name small{display:block;font-size:12px;font-weight:500;margin-top:4px}
.main-nav{position:absolute;left:452px;top:36px;display:flex;gap:0;font-size:13px;font-weight:500;color:var(--white);letter-spacing:.3px}
.main-nav span{margin-right:29px}
.dealer-login{position:absolute;left:932px;top:38px;font-size:11px;color:#a9d3f5;font-weight:500}
.sidebar{position:absolute;left:206px;top:128px;width:181px;font-size:12px}
.side-item{border-top:1px solid #8a8a8a;padding:4px 10px;color:var(--brand);font-weight:500}
.side-group{border-top:1px solid #8a8a8a;padding:4px 10px 4px 10px}
.side-group p{line-height:15px;margin-bottom:0}
.side-group .sub{padding-left:10px}
.side-group .current{color:var(--green)}
.side-group .dim{color:var(--muted)}
.side-group .gap{margin-top:6px}
.sidebar .last{border-top:1px solid #8a8a8a;height:1px}
.page-title{position:absolute;left:420px;top:70px;font-size:20px;font-weight:700;color:var(--brand)}
.crumbs{position:absolute;left:420px;top:96px;font-size:9px;color:#b5b5b5;line-height:13px}
.crumbs .here{color:var(--brand);padding-left:18px}
.crumbs i{font-style:normal;margin:0 5px}
.rule{position:absolute;left:420px;top:128px;width:609px;height:1px;background:#777}
.product-head{position:absolute;left:422px;top:129px;width:235px;height:40px;background:var(--brand-light);color:var(--white);font-size:12.5px;font-weight:700;padding:4px 16px;line-height:15px}
.tab{position:absolute;top:129px;height:40px;color:var(--white);font-size:10px;display:flex;align-items:center;justify-content:center}
.tab.overview{left:667px;width:80px;background:var(--tab-red)}
.tab.colors{left:752px;width:83px;background:var(--tab-violet)}
.photo{position:absolute;left:422px;top:175px;width:235px;height:246px;border:1px solid #ccc;display:flex;align-items:center;justify-content:center}
.photo .fill{width:190px;height:150px;background:linear-gradient(160deg,#a2492b,#7a2c18 55%,#2a2a2a)}
.thumb{position:absolute;top:425px;width:47px;height:49px;border:1px solid #ccc;padding:8px 5px}
.thumb .fill{width:100%;height:100%;background:linear-gradient(160deg,#a2492b,#3a2a24)}
.details{position:absolute;left:667px;top:175px;width:362px;height:451px;border:1px solid #ccc}
.details h2{position:absolute;left:13px;top:22px;font-size:12.5px;font-weight:700;letter-spacing:.2px}
.line-badge{position:absolute;left:268px;top:14px;display:flex;align-items:center;gap:4px;font-size:10px;color:#2b3b6b}
.line-badge b{width:22px;height:22px;border:1px solid #b44;border-radius:50%}
.features{position:absolute;left:16px;top:51px;width:300px;font-size:10.5px;color:var(--soft);line-height:13px}
.features p{margin-bottom:11px}
.pdf{position:absolute;left:270px;top:153px;width:77px;height:22px;background:var(--pdf);color:var(--white);font-size:9px;display:flex;align-items:center;justify-content:center}
.details h3{position:absolute;left:13px;top:188px;font-size:12.5px;font-weight:700}
.sizes{position:absolute;left:0;top:210px;width:362px;border-collapse:collapse;font-size:9.5px}
.sizes th{font-size:11px;font-weight:500;height:24px;text-align:center}
.sizes td{height:22px;border-top:1px solid #ccc;text-align:center}
.sizes td+td{border-left:1px solid #ccc}
.sizes tr:last-child td{border-bottom:1px solid #ccc}
.sizes .quote{color:var(--orange);font-weight:700;font-size:11.5px}
.site-footer{position:absolute;left:0;top:637px;width:1200px;height:113px;background:var(--brand);color:var(--white);font-size:13px}
.copyright{position:absolute;left:206px;top:55px}
.social{position:absolute;left:830px;top:55px;display:flex;gap:14px;align-items:center}
.social span{font-size:10px;font-weight:500}
</style>
</head>
<body>
<div class="page">
  <header class="site-header">
    <svg class="logo-fold" width="400" height="125" viewBox="0 0 400 125" aria-hidden="true">
      <polygon points="170,58 205,120 390,0 360,0" fill="#0560b4"/>
      <polygon points="170,58 205,120 205,58" fill="#0a74cf"/>
      <polygon points="205,120 390,0 300,58" fill="#0453a0"/>
    </svg>
    <div class="brand-name">KV<small>Homewares</small></div>
    <nav class="main-nav"><span>PRODUCTS</span><span>ORDERING</span><span>OUR COMPANY</span><span>FIND US</span></nav>
    <div class="dealer-login">DEALER'S LOGIN</div>
  </header>

  <aside class="sidebar">
    <div class="side-item">-&nbsp; Tables</div>
    <div class="side-group">
      <p>-&nbsp; Folding Tables</p>
      <p class="sub current">Laminate Surface Tables</p>
      <p class="sub dim">Plastic Tables</p>
      <p class="gap">+ Reception Tables</p>
      <p>+ Standing-up Meeting<br>&nbsp;&nbsp;&nbsp;Tables</p>
    </div>
    <div class="side-item">+ Seatings</div>
    <div class="side-item">+ Lecterns</div>
    <div class="side-item">+ Transport Solution</div>
    <div class="last"></div>
  </aside>

  <h1 class="page-title">TABLES</h1>
  <div class="crumbs">
    <div>&#8962;<i>›</i>Products<i>›</i>Tables<i>›</i>Folding Tables<i>›</i>EVOLVA Laminate Surface Tables</div>
    <div class="here">› EVOLVA Lightweight training tables - locking T-Leg</div>
  </div>
  <div class="rule"></div>

  <div class="product-head">Lightweight Training Tables<br>– Locking T-Leg</div>
  <div class="tab overview">OVERVIEW</div>
  <div class="tab colors">COLORS</div>

  <div class="photo"><div class="fill" role="img" aria-label="Cherry laminate training table with black locking T-legs and modesty panel"></div></div>
  <div class="thumb" style="left:422px"><div class="fill" role="img" aria-label="Training table front view thumbnail"></div></div>
  <div class="thumb" style="left:472px"><div class="fill" role="img" aria-label="Training table side view thumbnail"></div></div>

  <section class="details">
    <h2>EVOLVA™ TRAINING TABLES</h2>
    <div class="line-badge"><b></b>Evolva</div>
    <div class="features">
      <p>Lightweight Composite Core makes top up to 60%<br>lighter than other folding training tables</p>
      <p>Positive-Locking folding mechanism for simple &amp; safe operation</p>
      <p>Choice of Larkfield® high-pressure laminates</p>
      <p>TrimGuard® adds a perfect finish</p>
    </div>
    <div class="pdf">Download PDF</div>
    <h3>SIZES</h3>
    <table class="sizes">
      <tr><th>Model</th><th>Description</th><th>Weight</th><th></th></tr>
      <tr><td>EVO1860MXT</td><td>18" x 60" Training</td><td>30lbs</td><td class="quote">Request Quote</td></tr>
      <tr><td>EVO1872MXT</td><td>18" x 72" Training</td><td>35lbs</td><td class="quote">Request Quote</td></tr>
      <tr><td>EVO1896MXT</td><td>18" x 96" Training</td><td>41lbs</td><td class="quote">Request Quote</td></tr>
      <tr><td>EVO2460MXT</td><td>24" x 60" Training</td><td>35lbs</td><td class="quote">Request Quote</td></tr>
      <tr><td>EVO2472MXT</td><td>24" x 72" Training</td><td>38lbs</td><td class="quote">Request Quote</td></tr>
      <tr><td>EVO2496MXT</td><td>24" x 96" Training</td><td>45lbs</td><td class="quote">Request Quote</td></tr>
      <tr><td>EVO3060MXT</td><td>30" x 60" Banquet</td><td>40lbs</td><td class="quote">Request Quote</td></tr>
      <tr><td>EVO3072MXT</td><td>30" x 72" Banquet</td><td>44lbs</td><td class="quote">Request Quote</td></tr>
      <tr><td>EVO3096MXT</td><td>30" x 96" Banquet</td><td>51lbs</td><td class="quote">Request Quote</td></tr>
    </table>
  </section>

  <footer class="site-footer">
    <div class="copyright">© 2013 KV Homewares</div>
    <div class="social">Connect with us: <span>Linkmeet</span><span>Chirpo</span></div>
  </footer>
</div>
</body>
</html>
```